Tallow Roost Lead Generator + Checklist

I have typed up a 9 page word doc to be a lead generator for my website called "6 Simple Secrets Gala Hosts Love" and I am looking for someone to clean it up, and make it professional and inline with our brand.

Logo Hex: #971F20

Industry/Entity Type

Event Planning

Font styles to use
Other font styles liked:
• Helvetica Neue is our brands font, but it doesn't have to be that. Something similar that is rounded would be good like Arial I think.

Requirements
Must have
• Clean, but elegant design.
• Because it is very text heavy, have the topics easily broken out and maybe staggered so that it is easy to identify main topics and sub topics.
Should not have
• Not just looking for basic formating around the edges of the document, but to also have the text displayed in an easily readable way with clear sections.

```html
<!DOCTYPE html>
<html lang="en">
<head>
<meta charset="utf-8">
<title>Tallow Roost – 6 Simple Secrets Gala Hosts Love</title>
<link href="https://fonts.googleapis.com/css2?family=Arimo:ital,wght@0,400;0,700;1,400;1,700&family=Roboto:wght@300;900&display=swap" rel="stylesheet">
<style>
  :root {
    --brand-red: #971F20;
    --ink: #1d1d1d;
    --text: #2b2b2b;
    --ghost: #e4e4e6;
    --paper: #ffffff;
  }
  * { margin: 0; padding: 0; box-sizing: border-box; }
  html, body { width: 1200px; height: 777px; overflow: hidden; background: var(--paper); }
  body { font-family: "Arimo", Arial, sans-serif; color: var(--text); }
  .spread { position: relative; width: 1200px; height: 777px; overflow: hidden; }

  .page-left { position: absolute; left: 33px; top: 176px; width: 528px; }
  .intro-heading { font-size: 17.5px; font-weight: 700; color: var(--ink); margin-bottom: 13px; letter-spacing: -0.1px; }
  .body-copy { font-size: 11.2px; line-height: 13.6px; margin-bottom: 13.6px; }
  .body-copy strong { font-weight: 700; color: var(--ink); }
  .lead-in { font-size: 11.4px; line-height: 14px; font-weight: 700; color: var(--ink); margin-bottom: 14px; }

  .numbered { list-style: none; margin-left: 18px; }
  .numbered li { position: relative; padding-left: 18px; font-size: 11.2px; line-height: 13.6px; margin-bottom: 5.5px; }
  .numbered li .num { position: absolute; left: 0; top: 0; color: var(--brand-red); font-weight: 700; }

  .page-right { position: absolute; left: 642px; top: 58px; width: 524px; }
  .tips-title { font-family: "Roboto", Arial, sans-serif; font-weight: 300; font-size: 36px; line-height: 35px; color: var(--brand-red); letter-spacing: -1px; text-transform: uppercase; }
  .tips-title b { font-weight: 900; }
  .tip-bar { margin-top: 15px; height: 18px; background: var(--brand-red); color: #fff; font-weight: 700; font-size: 13.2px; line-height: 18px; padding-left: 5px; }
  .tip-bar .bar-num { display: inline-block; width: 33px; }
  .tip-body { margin-left: 38px; margin-top: 14px; }
  .tip-lead { font-size: 13px; line-height: 16px; font-weight: 700; color: var(--ink); margin-bottom: 7px; }
  .tip-lead em { font-style: italic; }
  .tip-body .numbered { margin-left: 22px; }
  .tip-body .numbered li { padding-left: 23px; margin-bottom: 5px; }
  .tip-close { font-size: 13px; line-height: 16px; font-weight: 700; color: var(--ink); margin-top: 2px; }

  .ghost-number { position: absolute; left: 632px; top: 535px; font-family: "Roboto", Arial, sans-serif; font-weight: 300; font-size: 290px; line-height: 1; color: var(--ghost); z-index: 0; }

  .folio { position: absolute; top: 740px; display: flex; align-items: center; gap: 6px; font-size: 7.4px; color: var(--ink); }
  .folio-left { left: 14px; }
  .folio-right { right: 14px; }
  .folio .mark { width: 14px; height: 14px; background: var(--brand-red); }
  .folio .page-no { color: var(--brand-red); font-weight: 700; }
</style>
</head>
<body>
<main class="spread">

  <section class="page-left">
    <h2 class="intro-heading">You have enough on your plate already.</h2>
    <p class="body-copy">The last thing you need is to waste time chasing down basic information from venues to try and present options to your boss, planning team or board. You could just go to the same place you always go to, but that gets old and you’d like to try something new.</p>
    <p class="body-copy">It seemed so easy, but a week goes by and you still don’t have good options because some venues still haven’t returned your calls and many of the venues website’s lack basic information about their private event space such as capacity, pricing and other important policies.</p>
    <p class="body-copy">You consider just driving to the venues to get the information, but who has five extra hours to do that? You definitely don’t.</p>
    <p class="body-copy">Don’t worry, <strong>you’re not alone.</strong> After planning many local events and experiencing that same back and forth with venues, I thought there had to be a better way. That’s why I created Tallow Roost and put together this guide with the help of other local leaders who have planned events in Juniper Falls.</p>
    <p class="lead-in">Here are the common mistakes we’ll go over, and how to avoid them so you’ll throw an event people will talk about for years.</p>
    <ol class="numbered">
      <li><span class="num">1.</span>As simple as it sounds - many planners don’t start by first thinking about the type of event they are planning, especially if is their first time planning an event.</li>
      <li><span class="num">2.</span>Often they don’t fully consider the expectations of their audience.</li>
      <li><span class="num">3.</span>Planners assume the policies from one venue to the next are similar, when in reality they can be very different - and they forget to ask the <em>right</em> questions.</li>
      <li><span class="num">4.</span>They forget that just like your car runs on gas, your event runs on great food and drinks.</li>
      <li><span class="num">5.</span>Lastly, they don’t track and ensure the details are completed.</li>
    </ol>
  </section>

  <div class="ghost-number" aria-hidden="true">1</div>

  <section class="page-right">
    <h1 class="tips-title">Here are the <b>5</b> simple tips to avoid these common mistakes</h1>
    <div class="tip-bar"><span class="bar-num">1.</span>Know the type of event you’re planning</div>
    <div class="tip-body">
      <p class="tip-lead">People who start planning an event without taking the time to think about the <em>type</em> of event they’re planning often run into problems.</p>
      <ol class="numbered">
        <li><span class="num">1.</span>For example, if you are planning a one time event and you aren’t regularly reaching out to your attendees and actively get the word out about the event, attendance will be low. If it is a recurring weekly event on the other hand, that level of communication probably isn’t needed as people will already be used to coming.</li>
        <li><span class="num">2.</span>I recently went to a one-time event and after registering didn’t hear anything from the event organizer, even on the day of the event! As an attendee I start to wonder if the event is even happening or not, I didn’t have a good feel for what to wear and I didn’t know which room to go to once I get to the venue. These are not the kind of thoughts you want running through your attendees heads just before the event, you want them excited and looking forward to your event - not uncertain about basic details.</li>
        <li><span class="num">3.</span>This might seem obvious, but it’s amazing how often this simple step of knowing the type of event you’re planning can get overlooked. It matters because the priorities and necessary steps for a recurring weekly networking event will be much different than a big end of year event.</li>
      </ol>
      <p class="tip-close">By knowing up front the type of event you’re planning - you’ll start looking at venues that are a great fit for that type of event and make sure you take the necessary steps to throw a great event!</p>
    </div>
  </section>

  <footer class="folio folio-left"><span class="mark"></span><span><span class="page-no">2</span> | Tallow Roost</span></footer>
  <footer class="folio folio-right"><span>6 Simple Secrets Gala Hosts Love &nbsp;| <span class="page-no">3</span></span><span class="mark"></span></footer>

</main>
</body>
</html>
```